Tactical Supply Company needing memorable business card design

Our tactical supply comapny is in need of a new business card design that will set us apart from the amateurs. We sell tactical gear ranging from backpacks and range bags to apparel and other gear. We are looking for a sharp design that incorporates our logo, website, and name. Our colors are white, red, and black, or any combination of the three, preferably red and black.
I have attached our logo with our name underneath but I have also edited that design with the logo incorporated next to the name (attached).

Target Market(s)

Law enforcement, military, tactical

Industry/Entity Type

Business

Contact Information for Business Card

Include www.brindlequarry.example

Colors
000000
ec1f27
ffffff

Requirements
Must have
• Our name, logo, and website. This is intended to be a memorable simple card, no name, address, email, or phone number info is necessary. Designs that do include this additional info will still be considered if they are absolutely spectacular.
Should not have
• A standard template design, I can create that in my own on Cardomix. I am looking for a new, creative design that is completely unique to my company.

```html
<!DOCTYPE html>
<html lang="en">
<head>
<meta charset="utf-8">
<title>Brindle Quarry Tactical Supply – Business Card</title>
<link href="https://fonts.googleapis.com/css2?family=Exo+2:wght@500;600;700&display=swap" rel="stylesheet">
<style>
  :root {
    --stage: #3a3330;
    --card: #121212;
    --card-edge: #1c1c1c;
    --red: #ec1f27;
    --white: #ffffff;
    --silver: #c9c9c9;
  }
  * { margin: 0; padding: 0; box-sizing: border-box; }
  html, body { width: 1200px; height: 780px; overflow: hidden; }
  body {
    background: var(--stage);
    font-family: "Exo 2", sans-serif;
    display: flex;
    align-items: center;
    justify-content: center;
    gap: 50px;
  }
  .card {
    width: 540px;
    height: 309px;
    background: var(--card);
    border: 1px solid var(--card-edge);
    position: relative;
    color: var(--white);
    box-shadow: 0 10px 30px rgba(0,0,0,.45);
  }
  .brand {
    display: flex;
    align-items: center;
    gap: 12px;
  }
  .brand-square {
    width: 34px;
    height: 34px;
    background: var(--red);
  }
  .brand-name {
    font-weight: 700;
    font-size: 34px;
    letter-spacing: 1px;
    text-transform: uppercase;
    color: var(--white);
    line-height: 1;
  }
  .brand-tagline {
    font-weight: 600;
    font-size: 12px;
    letter-spacing: 4px;
    text-transform: uppercase;
    color: var(--silver);
    margin-top: 8px;
    text-align: center;
  }
  /* Front */
  .card-front .brand-block {
    position: absolute;
    top: 50%;
    left: 50%;
    transform: translate(-50%, -50%);
    display: flex;
    flex-direction: column;
    align-items: center;
  }
  /* Back */
  .card-back .brand-block {
    position: absolute;
    top: 52px;
    right: 40px;
    display: flex;
    flex-direction: column;
    align-items: flex-end;
  }
  .card-back .brand-name { font-size: 30px; }
  .card-back .brand-square { width: 30px; height: 30px; }
  .person {
    position: absolute;
    left: 36px;
    top: 178px;
    width: 220px;
    text-align: right;
  }
  .person-name { color: var(--red); font-weight: 700; font-size: 22px; line-height: 1.1; }
  .person-title { font-weight: 500; font-size: 14px; margin-top: 4px; }
  .person-address { font-weight: 500; font-size: 13px; margin-top: 4px; }
  .divider {
    position: absolute;
    left: 272px;
    top: 180px;
    width: 2px;
    height: 74px;
    background: var(--silver);
  }
  .contacts {
    position: absolute;
    left: 290px;
    top: 182px;
    list-style: none;
  }
  .contacts li {
    display: flex;
    align-items: center;
    gap: 9px;
    font-weight: 500;
    font-size: 14px;
    margin-bottom: 8px;
  }
  .contacts svg { width: 16px; height: 16px; flex: none; }
</style>
</head>
<body>
  <section class="card card-front">
    <div class="brand-block">
      <div class="brand">
        <span class="brand-square"></span>
        <span class="brand-name">Brindle Quarry</span>
      </div>
      <div class="brand-tagline">Tactical Supply</div>
    </div>
  </section>

  <section class="card card-back">
    <div class="brand-block">
      <div class="brand">
        <span class="brand-square"></span>
        <span class="brand-name">Brindle Quarry</span>
      </div>
      <div class="brand-tagline">Tactical Supply</div>
    </div>

    <div class="person">
      <div class="person-name">Employee Name</div>
      <div class="person-title">Managing Director</div>
      <div class="person-address">Harlow Creek, Vermont 05821</div>
    </div>

    <div class="divider"></div>

    <ul class="contacts">
      <li>
        <svg viewBox="0 0 16 16" aria-hidden="true"><rect width="16" height="16" rx="3" fill="#ec1f27"/><path d="M5 3.5l2 2-1 1.2c.6 1.3 1.6 2.3 2.9 2.9l1.2-1 2 2-1.3 1.4C7.6 11.6 4.4 8.4 3.6 4.8z" fill="#fff"/></svg>
        0155 0142 736
      </li>
      <li>
        <svg viewBox="0 0 16 16" aria-hidden="true"><rect width="16" height="16" rx="3" fill="#ec1f27"/><rect x="3" y="4.5" width="10" height="7" fill="#fff"/><path d="M3 4.5l5 4 5-4" fill="none" stroke="#ec1f27" stroke-width="1.2"/></svg>
        hello@brindlequarry.example
      </li>
      <li>
        <svg viewBox="0 0 16 16" aria-hidden="true"><rect width="16" height="16" rx="3" fill="#ec1f27"/><circle cx="8" cy="8" r="4.8" fill="none" stroke="#fff" stroke-width="1.2"/><path d="M3.2 8h9.6M8 3.2c-2 2.6-2 7 0 9.6M8 3.2c2 2.6 2 7 0 9.6" fill="none" stroke="#fff" stroke-width="1"/></svg>
        www.brindlequarry.example
      </li>
    </ul>
  </section>
</body>
</html>
```